A Business Card and Letterhead for a Surgeon in Practice

Design a Business Card and Business Letterhead with theming consistent with my website, logo and referral pad which will be uploaded for reference.

Website found at: www.brendamarlow.com.au

A text file is uploaded indicating what information needs to be on the business card and a separate document for the letterhead.

The other images I have uploaded are entirely optional for artistic design. None of them necessarily have to be used. Further imagery may or may not be included as per the designer to get the best result
Updates

Industry/Entity Type

Medical

Requirements
Must have
• Logo as uploaded. Certain text as uploaded.
• NEW as of 8th August:
• **On the back there needs to be a blank space incorporating at least half of the vertical distance of the card - this is where stickers can be placed in the office for certain appointment details**
• **Also, for the consulting locations a small box next to each should be included so that it can be ticked by my secretary indicating the correct location**

```html
<!DOCTYPE html>
<html lang="en">
<head>
<meta charset="utf-8">
<title>Brenda Marlow – Letterhead</title>
<link href="https://fonts.googleapis.com/css2?family=Roboto:wght@400;500&display=swap" rel="stylesheet">
<style>
  :root {
    --teal: #168a83;
    --teal-bright: #009279;
    --charcoal: #36302e;
    --grey: #7a7a7a;
    --ink: #1e1e1e;
    --white: #ffffff;
  }
  * { margin: 0; padding: 0; box-sizing: border-box; }
  html, body { width: 848px; height: 1200px; overflow: hidden; background: var(--white); }
  body { font-family: "Roboto", Arial, sans-serif; }
  .letterhead { position: relative; width: 848px; height: 1200px; overflow: hidden; background: var(--white); }
  .shapes { position: absolute; inset: 0; }
  .brand { position: absolute; left: 28px; top: 34px; display: flex; align-items: center; gap: 14px; }
  .brand-dot { width: 72px; height: 72px; border-radius: 50%; background: var(--teal); }
  .brand-name { font-size: 33px; font-weight: 400; color: var(--teal); text-transform: uppercase; letter-spacing: 1px; line-height: 1; }
  .brand-role { font-size: 11px; color: var(--grey); letter-spacing: 2.6px; text-transform: uppercase; margin-top: 6px; }
  .header-info { position: absolute; left: 590px; width: 244px; top: 12px; text-align: center; color: var(--white); font-size: 11px; line-height: 10.5px; white-space: nowrap; }
  .header-info .gap { height: 11px; }
  .header-info .gap-lg { height: 24px; }
  .web { position: absolute; top: 1028px; left: 0; width: 848px; text-align: center; font-size: 15px; letter-spacing: 4.2px; color: var(--ink); padding-left: 48px; }
  .col-title { font-size: 11px; letter-spacing: 1.2px; text-decoration: underline; text-underline-offset: 2px; color: var(--ink); }
  .operating { position: absolute; right: 680px; top: 1096px; text-align: right; font-size: 11.5px; letter-spacing: 0.8px; line-height: 12px; color: var(--ink); white-space: nowrap; }
  .operating .col-title { margin-bottom: 7px; }
  .consulting { position: absolute; left: 178px; top: 1096px; font-size: 11.5px; letter-spacing: 1px; line-height: 12px; color: #333; white-space: nowrap; }
  .consulting .col-title { margin-bottom: 11px; color: #333; }
  .consulting .row { display: flex; }
  .consulting .region { width: 73px; }
  .contact { position: absolute; right: 19px; top: 1088px; text-align: right; color: var(--white); font-size: 11.5px; line-height: 10.5px; white-space: nowrap; }
  .contact .strong { font-weight: 500; }
  .contact .split { display: flex; justify-content: space-between; gap: 40px; }
  .contact .small { font-size: 9.5px; line-height: 10px; }
  .contact .gap { height: 10px; }
  .contact .email { margin-top: 14px; font-size: 11px; }
</style>
</head>
<body>
<div class="letterhead">
  <svg class="shapes" width="848" height="1200" viewBox="0 0 848 1200" aria-hidden="true">
    <path d="M504 0 Q494 80 510 154 L848 154 L848 0 Z" fill="var(--teal)"/>
    <path d="M568 0 Q532 80 540 154 L848 154 L848 0 Z" fill="var(--charcoal)"/>
    <rect x="0" y="154" width="848" height="12" fill="var(--teal)"/>
    <rect x="0" y="166" width="848" height="6" fill="var(--charcoal)"/>
    <rect x="0" y="1020" width="848" height="6" fill="var(--charcoal)"/>
    <rect x="0" y="1046" width="848" height="7" fill="var(--charcoal)"/>
    <rect x="0" y="1053" width="848" height="6" fill="var(--teal)"/>
    <path d="M498 1053 Q462 1120 452 1200 L848 1200 L848 1053 Z" fill="var(--teal-bright)"/>
    <path d="M590 1053 Q550 1120 538 1200 L848 1200 L848 1053 Z" fill="var(--charcoal)"/>
  </svg>

  <header>
    <div class="brand">
      <div class="brand-dot"></div>
      <div>
        <div class="brand-name">Brenda Marlow</div>
        <div class="brand-role">General, Upper GI &amp; Bariatric Surgeon</div>
      </div>
    </div>
    <div class="header-info">
      <p>DR BRENDA MARLOW ABN 48 602 115 937</p>
      <div class="gap"></div>
      <p>Services :</p>
      <div class="gap"></div>
      <p>Bariatric Surgery</p>
      <p>General Surgery</p>
      <p>Antireflux Surgery</p>
      <p>Body Contouring Surgery</p>
      <div class="gap-lg"></div>
      <p>Dr Brenda Marlow MBBS FRACS Grad Cert</p>
      <p>General, Upper GI, &amp; Obesity Surgeon</p>
    </div>
  </header>

  <footer>
    <div class="web">www.brendamarlow.com.au</div>
    <div class="operating">
      <div class="col-title">OPERATING</div>
      <p>Fernvale Eastern Hospital</p>
      <p>Yarra Bend Private</p>
      <p>Kingsley Hill Hospital</p>
      <p>Coastal Plains Hospital</p>
    </div>
    <div class="consulting">
      <div class="col-title">CONSULTING</div>
      <div class="row"><span class="region">Melbourne</span><span>: Market St CBD, Elmwood, Ashgrove.</span></div>
      <div class="row"><span class="region">Regional</span><span>: Redgum, Millbrook, Valley Plains.</span></div>
    </div>
    <div class="contact">
      <p class="strong">Fernvale Eastern Hospital</p>
      <p>Suite 14, 3rd Floor, 9 Linden St, Fernvale 3190</p>
      <p class="split"><span>Tel: 03 9000 4182</span><span>Fax: 03 9000 4183</span></p>
      <p>Paging Service : 0400 118 262</p>
      <div class="gap"></div>
      <p class="small">All Appointments &amp; Correspondence to Fernvale Rooms</p>
      <p>Provider No. 481257KT</p>
      <p class="email">Email: info@marlowsurgicalcare.com.au</p>
    </div>
  </footer>
</div>
</body>
</html>
```